Webdesign project for healthcare IT company

Home, About, Solution, Contact, and Employment pages.

Please match the designs uploaded for colors and effect.

Please choose appropriate healthcare IT related photos to the content. Be sure to include the content that i've attached in the word document.

Please use the following URLs as reference:

www.veltrocare.example
www.dusk.example
www.plainagree.example

Target Market(s)

healthcare providers, doctors, nurses, c-level executives

Industry/Entity Type

Healthcare

Coding

Coded - Design and coding required

Number of Pages Required

5+ page

Font styles to use
Serif
Sans Serif

Colors
6b449b
0455a3
ffffff
333333
959595

Requirements
Must have
• B2B feel, matches the colors in the uploaded design files, images that can be purchased later that meet the content that I've uploaded

```html
<!DOCTYPE html>
<html lang="en">
<head>
<meta charset="utf-8">
<title>Vireo Technologies – Home</title>
<link href="https://fonts.googleapis.com/css2?family=Lato:wght@300;400;700;900&display=swap" rel="stylesheet">
<style>
:root{
  --purple:#6b449b;
  --blue:#0455a3;
  --navy:#2e2a5e;
  --indigo:#3a2c64;
  --white:#ffffff;
  --ink:#333333;
  --grey:#959595;
  --mist:#e9e9ea;
}
*{box-sizing:border-box;margin:0;padding:0}
html,body{width:1200px;height:2403px;overflow:hidden}
body{font-family:'Lato',Arial,sans-serif;color:var(--ink);background:var(--white);position:relative}
.abs{position:absolute}

/* Hero */
.hero{position:absolute;left:0;top:0;width:1200px;height:665px;overflow:hidden}
.hero-photo{position:absolute;inset:0;background:
  radial-gradient(ellipse at 70% 40%,#c9d0d6 0%,#8e9aa5 35%,#4f5a66 75%,#343c46 100%)}
.hero-shade{position:absolute;inset:0;background:rgba(20,25,35,.38)}
.brand{position:absolute;display:flex;align-items:center;gap:12px;font-weight:700;letter-spacing:1px}
.brand-mark{width:26px;height:26px;background:var(--purple);border-radius:50%}
.brand-name{font-size:30px;line-height:1}
.hero .brand{left:128px;top:42px;color:var(--white)}
.nav-bar{position:absolute;left:521px;top:0;width:60px;height:4px;background:var(--white)}
.nav{position:absolute;top:50px;right:119px;display:flex;gap:38px;list-style:none}
.nav a{color:var(--white);text-decoration:none;font-size:16px;font-weight:400;letter-spacing:.3px}
.hero-title{position:absolute;left:0;width:1200px;top:232px;text-align:center;color:var(--white);font-weight:700;font-size:42px;line-height:48px;letter-spacing:.3px}
.hero-lede{position:absolute;left:160px;width:880px;top:356px;text-align:center;color:var(--white);font-size:17px;line-height:29px}
.scroll-down{position:absolute;left:574px;top:500px;width:50px;height:50px;border:2px solid var(--white);border-radius:50%}
.dots{position:absolute;left:1085px;top:296px;display:flex;flex-direction:column;gap:10px}
.dots span{width:14px;height:14px;border-radius:50%;background:var(--white)}
.dots span:first-child{background:transparent;border:2px solid var(--white)}

/* What we do */
.section-title{position:absolute;left:0;width:1200px;text-align:center;font-weight:700;font-size:29px}
.what .section-title{top:778px;color:#111}
.what-body{position:absolute;left:112px;width:976px;top:836px;text-align:center;font-size:15.5px;line-height:25.6px;color:#444}
.what-body p{margin-bottom:13px}

/* Solutions band */
.band{position:absolute;left:0;top:1118px;width:1200px;height:492px;background:linear-gradient(120deg,#1a56a8 0%,#24469a 50%,#2e2f6e 100%)}
.card{position:absolute;top:75px;width:303px;height:351px;border:1px solid rgba(255,255,255,.7);background:rgba(255,255,255,.03);color:var(--white);text-align:center}
.card-photo{height:180px}
.card h3{font-size:21px;font-weight:700;margin-top:20px}
.card p{font-size:14.5px;line-height:22px;padding:8px 34px 0;color:#e4e6f2}
.photo-retro{background:linear-gradient(160deg,#f2f2f0,#cfcbc0)}
.photo-checkin{background:linear-gradient(160deg,#d6d8dc,#8a8f96)}
.photo-print{background:linear-gradient(160deg,#c7d3f2,#3f5fd0)}

/* Contact */
.contact{position:absolute;left:0;top:1610px;width:1200px;height:441px;background:var(--mist)}
.map{position:absolute;left:140px;top:40px;width:920px;height:370px;background:radial-gradient(ellipse at center,#dcdcde 0%,rgba(233,233,234,0) 70%)}
.contact .section-title{top:90px;color:var(--blue);font-size:29px}
.channel{position:absolute;top:162px;width:300px;text-align:center}
.ring{width:104px;height:104px;margin:0 auto;border:2px solid var(--c);border-radius:50%;padding:7px}
.ring div{width:100%;height:100%;border-radius:50%;background:var(--c);display:flex;align-items:center;justify-content:center}
.channel h4{font-weight:400;font-size:21px;color:var(--c);margin-top:20px}
.channel p{font-size:18px;color:#111;margin-top:4px}

/* Footer */
.footer .brand{left:141px;top:2155px;color:var(--purple)}
.foot-col{position:absolute;top:2122px}
.foot-col h5{font-size:17px;font-weight:700;color:#111;margin-bottom:18px}
.foot-col ul{list-style:none}
.foot-col li{font-size:14px;color:#666;line-height:28.8px}
.social{display:flex;gap:8px}
.social span{width:42px;height:42px;border:2px solid var(--indigo);border-radius:50%}
.legal{position:absolute;left:0;top:2339px;width:1200px;height:64px;background:var(--navy);color:#c9c7dc;font-size:13px;padding:22px 144px}
</style>
</head>
<body>

<header class="hero">
  <div class="hero-photo" role="img" aria-label="Photo of a doctor and clinicians reviewing records on a tablet in a hospital"></div>
  <div class="hero-shade"></div>
  <div class="brand"><span class="brand-mark"></span><span class="brand-name">Vireo Technologies</span></div>
  <div class="nav-bar"></div>
  <ul class="nav">
    <li><a href="#">HOME</a></li>
    <li><a href="#">ABOUT</a></li>
    <li><a href="#">SOLUTION</a></li>
    <li><a href="#">EMPLOYMENT</a></li>
    <li><a href="#">CONTACT</a></li>
  </ul>
  <h1 class="hero-title">IT’S TIME TO WAKE UP WITH<br>VIREO TECHNOLOGIES</h1>
  <p class="hero-lede">Disruption isn’t just coming – it’s already here and it’s time to wake up to the new world we live in. Here at Vireo Technologies, we embrace the future that disruption brings and make it our aim to assist the world in embracing this bright future with us. We help bring businesses and people adapt to new approaches to old problems.</p>
  <div class="scroll-down">
    <svg width="46" height="46" viewBox="0 0 46 46"><path d="M16 20l7 7 7-7" fill="none" stroke="#fff" stroke-width="2.5" stroke-linecap="round" stroke-linejoin="round"/></svg>
  </div>
  <div class="dots"><span></span><span></span><span></span><span></span></div>
</header>

<section class="what">
  <h2 class="section-title">WHAT WE DO</h2>
  <div class="what-body">
    <p>We are engineers, problem-solvers, people persons, and a friendly face. We want to solve your problem in a way that won’t break the bank, give headaches, leave you with a smile on your face, and keep you smiling throughout our relationship.</p>
    <p>We predominantly work in the healthcare IT industry assisting hospitals and clinics with their IT infrastructure and information workflows. We provide software solutions and interoperability services to connect platforms and give care givers a simple view of patient records.</p>
    <p>Vireo Technologies is also exploring the world of 3D printing and how it can fully affect the healthcare industry and small businesses with Vireo3D. 3D printing is a great solution to what used to be a very niche industry.</p>
  </div>
</section>

<section class="band">
  <article class="card" style="left:120px">
    <div class="card-photo photo-retro" role="img" aria-label="Photo of a vintage desktop computer"></div>
    <h3>Computer Archeology</h3>
    <p>Need data off a legacy system that you would like to sunset? We can help you with that.</p>
  </article>
  <article class="card" style="left:449px">
    <div class="card-photo photo-checkin" role="img" aria-label="Photo of a patient checking in on a tablet"></div>
    <h3>Digital Check In</h3>
    <p>Still using clipboards to check people into your facility? Struggling to get that paper-based information into your system? We can help you with that.</p>
  </article>
  <article class="card" style="left:774px">
    <div class="card-photo photo-print" role="img" aria-label="Photo of a 3D printer printing a blue object"></div>
    <h3>Vireo3D</h3>
    <p>Have something in mind that you need printed, but don’t have a 3D printer? We can help you design it, and print it for you.</p>
  </article>
</section>

<section class="contact">
  <div class="map" role="img" aria-label="Faint world map background"></div>
  <h2 class="section-title">CONTACT US</h2>
  <div class="channel" style="left:158px;--c:#1a56a8">
    <div class="ring"><div>
      <svg width="30" height="30" viewBox="0 0 24 24"><path d="M12 2a7 7 0 0 0-7 7c0 5 7 13 7 13s7-8 7-13a7 7 0 0 0-7-7zm0 9.5A2.5 2.5 0 1 1 12 6.5a2.5 2.5 0 0 1 0 5z" fill="#fff"/></svg>
    </div></div>
    <h4>(DIRECT)</h4>
    <p>+1 (555) 014-2298</p>
  </div>
  <div class="channel" style="left:464px;--c:#5b46a0">
    <div class="ring"><div>
      <svg width="30" height="30" viewBox="0 0 24 24"><path d="M6.6 10.8a15.1 15.1 0 0 0 6.6 6.6l2.2-2.2a1 1 0 0 1 1-.25 11.4 11.4 0 0 0 3.6.57 1 1 0 0 1 1 1V20a1 1 0 0 1-1 1A17 17 0 0 1 3 4a1 1 0 0 1 1-1h3.5a1 1 0 0 1 1 1c0 1.25.2 2.45.57 3.57a1 1 0 0 1-.25 1z" fill="#fff"/></svg>
    </div></div>
    <h4>Main</h4>
    <p style="font-size:21px">+1 (555) 017-3340</p>
  </div>
  <div class="channel" style="left:758px;--c:#3a2c64">
    <div class="ring"><div>
      <svg width="30" height="30" viewBox="0 0 24 24"><path d="M3 5h18v14H3z" fill="#fff"/><path d="M3 5l9 7 9-7" fill="none" stroke="#3a2c64" stroke-width="1.8"/></svg>
    </div></div>
    <h4>Email Us</h4>
    <p>mara@vireotech.example</p>
  </div>
</section>

<footer class="footer">
  <div class="brand"><span class="brand-mark"></span><span class="brand-name">Vireo Technologies</span></div>
  <div class="foot-col" style="left:487px">
    <h5>COMPANY</h5>
    <ul><li>Home</li><li>About</li><li>Solution</li><li>Employment</li></ul>
  </div>
  <div class="foot-col" style="left:675px;top:2118px">
    <h5>RESOURCES</h5>
    <ul><li>Sitemap</li><li>Blogs</li><li>News</li><li>Contact</li></ul>
  </div>
  <div class="foot-col" style="left:870px;top:2118px">
    <h5 style="font-size:16px">FOLLOW US</h5>
    <div class="social">
      <span aria-label="Social profile 1"></span>
      <span aria-label="Social profile 2"></span>
      <span aria-label="Social profile 3"></span>
    </div>
  </div>
  <div class="legal">© 2018 Company Name&nbsp; All right reserved</div>
</footer>

</body>
</html>
```